Calvanta Group Real Estate Company business cards

New business card design, we are generally happy with the basic layout of the existing front of business card, (feel free to change) but require a head shot photo on the back side.

http://www.calvanta.com.au/

Attached logos, and existing business card

------------------------------

Target Market(s)

Real estate

Industry/Entity Type

Real Estate

Contact Information for Business Card

Standard size double sided

Font styles to use
Other font styles liked:
• Futura

Requirements
Must have
• Photo head shot on the back side
Nice to have
• yes
Should not have
• No

```html
<!DOCTYPE html>
<html lang="en">
<head>
<meta charset="utf-8">
<title>Calvanta Group business cards</title>
<link href="https://fonts.googleapis.com/css2?family=Jost:wght@400;500;600&display=swap" rel="stylesheet">
<style>
  :root {
    --backdrop: #2b2d2c;
    --card: #f4f4f3;
    --brand-purple: #2d1a5e;
    --brand-orange: #f0901e;
    --ink: #1c1a2a;
    --rule: #6a5a9a;
    --photo-top: #e9e9ea;
    --photo-mid: #8f8c92;
    --photo-suit: #25304f;
  }
  * { margin: 0; padding: 0; box-sizing: border-box; }
  html, body { width: 1200px; height: 1019px; overflow: hidden; }
  body {
    background: var(--backdrop);
    font-family: "Jost", "Futura", sans-serif;
    color: var(--ink);
    position: relative;
  }
  .card {
    position: absolute;
    top: 330px;
    width: 527px;
    height: 340px;
    background: var(--card);
    overflow: hidden;
  }
  .card--front { left: 66px; }
  .card--back { left: 607px; }

  .wordmark {
    position: absolute;
    display: flex;
    align-items: center;
    gap: 8px;
    color: var(--brand-purple);
    font-weight: 500;
    white-space: nowrap;
  }
  .wordmark__dot {
    width: 10px; height: 10px;
    background: var(--brand-orange);
  }
  .card--front .wordmark { left: 18px; top: 160px; font-size: 28px; }
  .card--back .wordmark { left: 49px; top: 132px; font-size: 36px; }

  .divider {
    position: absolute;
    left: 254px; top: 102px;
    width: 1.5px; height: 144px;
    background: linear-gradient(to bottom, transparent, var(--rule) 15%, var(--rule) 85%, transparent);
  }
  .details {
    position: absolute;
    left: 268px; top: 108px;
    font-size: 14px;
    line-height: 1.2;
  }
  .details__name { font-weight: 600; color: var(--brand-purple); font-size: 15px; }
  .details__role { font-weight: 400; font-size: 13px; }
  .details__company { margin-top: 10px; }
  .contact-list { list-style: none; margin-top: 10px; }
  .contact-list li { display: flex; align-items: center; gap: 6px; height: 19px; }
  .contact-list svg { width: 12px; height: 12px; flex: none; }

  .services {
    position: absolute;
    left: 114px; top: 238px;
    font-size: 15px;
    font-weight: 500;
    letter-spacing: 0.3px;
  }
  .headshot {
    position: absolute;
    right: 0; top: 0;
    width: 184px; height: 340px;
    background: linear-gradient(to bottom, var(--photo-top) 0%, var(--photo-mid) 45%, var(--photo-suit) 62%, var(--photo-suit) 100%);
  }
</style>
</head>
<body>
  <section class="card card--front">
    <div class="wordmark"><span class="wordmark__dot"></span>Calvanta Group</div>
    <div class="divider"></div>
    <div class="details">
      <p><span class="details__name">Daniel Tran</span> <span class="details__role">| Director</span></p>
      <p class="details__company">Calvanta Group<br>ABN: 12 345 678 901</p>
      <ul class="contact-list">
        <li>
          <svg viewBox="0 0 12 12"><rect x="3" y="1" width="6" height="10" rx="1" fill="none" stroke="#2d1a5e" stroke-width="1.2" transform="skewX(-10)"/></svg>
          0412 555 018
        </li>
        <li>
          <svg viewBox="0 0 12 12"><rect x="1" y="3" width="10" height="7" fill="#2d1a5e"/><path d="M1 3 L6 7 L11 3" fill="none" stroke="#f4f4f3" stroke-width="1"/></svg>
          daniel.tran@calvanta.com.au
        </li>
        <li>
          <svg viewBox="0 0 12 12"><circle cx="6" cy="6" r="5" fill="#2d1a5e"/><path d="M1 6 H11 M6 1 V11" stroke="#f4f4f3" stroke-width="0.7"/><ellipse cx="6" cy="6" rx="2.3" ry="5" fill="none" stroke="#f4f4f3" stroke-width="0.7"/></svg>
          www.calvanta.com.au
        </li>
      </ul>
    </div>
  </section>

  <section class="card card--back">
    <div class="wordmark"><span class="wordmark__dot"></span>Calvanta Group</div>
    <p class="services">BUY | SELL | RENT</p>
    <div class="headshot" role="img" aria-label="Head shot of the director in a navy suit and blue tie"></div>
  </section>
</body>
</html>
```